Logo and business card design

Business name: Merrick Hale Consulting Inc.
Card holder name: XXXXXX J Hale, PMP
Title: Principal
Email: [url removed, login to view]@[url removed, login to view]
Phone: (555) 013-2748
Website: [url removed, login to view]

Please also incorporate the following on the card, in some way (feel free to be creative and/or use the back of the card):

35+ years experience in Civil Infrastructure Construction & Maintenance
Code of Practice: Honesty, Integrity & Respect

It may be tough to fit all of the above on the card, so feel free to paraphrase or be creative to get the point across without being verbatim.

The business card should also incorporate a unique logo which isn't plagiarized.

Here are some links to give you an idea of brands/logos I like:

[url removed, login to view]

I'm looking for something modern and not too complicated.

Thanks and good luck!

```html
<!DOCTYPE html>
<html lang="en">
<head>
<meta charset="utf-8">
<title>Merrick Hale Consulting Inc. — Logo and Business Cards</title>
<link rel="stylesheet" href="https://fonts.googleapis.com/css2?family=Exo+2:wght@400;500;700&display=swap">
<style>
  :root {
    --stage: #262626;
    --black: #000000;
    --white: #ffffff;
    --blue: #21aee8;
    --sky: #0ba3e6;
    --grey: #8f8f8f;
    --grey-dark: #5c5c5c;
    --ink: #1b1b1b;
    --navy: #0b2a44;
  }
  * { box-sizing: border-box; margin: 0; padding: 0; }
  html, body { width: 870px; height: 1200px; overflow: hidden; }
  body {
    position: relative;
    background: var(--stage);
    font-family: "Exo 2", sans-serif;
  }

  .brand-banner {
    position: absolute; left: 0; top: 0; width: 870px; height: 225px;
    background: var(--black);
    display: flex; align-items: center; justify-content: center; gap: 26px;
  }
  .brand-banner .brand-square { width: 58px; height: 58px; background: var(--blue); }
  .brand-banner .brand-name {
    color: var(--blue); font-weight: 700; font-size: 46px; letter-spacing: 2px;
    text-transform: uppercase; line-height: 1.1;
  }

  .business-card {
    position: absolute; width: 517px; height: 290px;
  }
  .card--white { left: 51px; top: 251px; background: var(--white); }
  .card--black { left: 317px; top: 563px; background: var(--black); }
  .card--blue  { left: 51px; top: 867px; background: var(--sky); }

  .card-brand {
    position: absolute; left: 30px; top: 78px; width: 210px;
    display: flex; align-items: center; gap: 10px;
  }
  .card-brand .brand-square { width: 22px; height: 22px; flex: none; }
  .card-brand .brand-name {
    font-weight: 700; font-size: 19px; letter-spacing: 0.5px; line-height: 1.15;
    text-transform: uppercase;
  }
  .card--white .brand-square, .card--black .brand-square { background: var(--blue); }
  .card--white .brand-name, .card--black .brand-name { color: var(--blue); }
  .card--blue .brand-square { background: var(--white); }
  .card--blue .brand-name { color: var(--white); }

  .card-divider {
    position: absolute; left: 259px; top: 40px; width: 1px; height: 150px;
  }
  .card--white .card-divider { background: #cfcfcf; }
  .card--black .card-divider { background: #3a3a3a; }
  .card--blue .card-divider { background: rgba(255,255,255,0.55); }

  .card-holder { position: absolute; left: 303px; top: 42px; }
  .holder-name { font-size: 14px; font-weight: 400; }
  .holder-title { font-size: 19px; font-weight: 400; margin-top: 3px; }
  .card--white .holder-name { color: var(--grey-dark); }
  .card--black .holder-name { color: var(--grey); }
  .card--white .holder-title, .card--black .holder-title { color: var(--blue); }
  .card--blue .holder-name { color: var(--white); }
  .card--blue .holder-title { color: var(--ink); }

  .contact-list { position: absolute; left: 303px; top: 116px; list-style: none; }
  .contact-list li {
    display: flex; align-items: center; gap: 9px;
    font-size: 11.5px; height: 26px;
  }
  .contact-list svg { width: 12px; height: 12px; flex: none; }
  .card--white .contact-list li { color: var(--grey-dark); }
  .card--black .contact-list li { color: var(--grey); }
  .card--blue .contact-list li { color: var(--navy); }
  .card--white .contact-list svg, .card--black .contact-list svg { color: var(--blue); }
  .card--blue .contact-list svg { color: var(--white); }

  .card-values {
    position: absolute; left: 0; right: 0; top: 232px; text-align: center;
  }
  .values-line { font-size: 15px; letter-spacing: 2px; }
  .values-line .dot {
    display: inline-block; width: 4px; height: 4px; margin: 0 5px; vertical-align: middle;
    background: var(--blue);
  }
  .experience-line { font-size: 10px; margin-top: 3px; letter-spacing: 0.2px; }
  .card--white .values-line { color: var(--grey-dark); }
  .card--black .values-line { color: var(--grey-dark); }
  .card--blue .values-line { color: var(--white); }
  .card--blue .values-line .dot { background: var(--navy); }
  .experience-line .accent { color: var(--blue); }
  .card--white .experience-line .plain { color: var(--grey-dark); }
  .card--black .experience-line .plain { color: var(--white); }
  .card--blue .experience-line .accent { color: var(--ink); }
  .card--blue .experience-line .plain { color: var(--white); }
</style>
</head>
<body>

<svg width="0" height="0" style="position:absolute">
  <defs>
    <symbol id="icon-phone" viewBox="0 0 12 12">
      <rect x="3" y="0.5" width="6" height="11" rx="1.2" fill="currentColor"/>
      <rect x="4.2" y="2" width="3.6" height="4.5" fill="#fff" opacity="0.8"/>
    </symbol>
    <symbol id="icon-mail" viewBox="0 0 12 12">
      <rect x="0.7" y="2.2" width="10.6" height="7.6" fill="none" stroke="currentColor" stroke-width="1.2"/>
      <path d="M0.9 2.6 L6 6.6 L11.1 2.6" fill="none" stroke="currentColor" stroke-width="1.2"/>
    </symbol>
    <symbol id="icon-web" viewBox="0 0 12 12">
      <circle cx="6" cy="6" r="5.2" fill="none" stroke="currentColor" stroke-width="1.1"/>
      <ellipse cx="6" cy="6" rx="2.3" ry="5.2" fill="none" stroke="currentColor" stroke-width="1"/>
      <line x1="0.8" y1="6" x2="11.2" y2="6" stroke="currentColor" stroke-width="1"/>
    </symbol>
  </defs>
</svg>

<header class="brand-banner">
  <span class="brand-square"></span>
  <span class="brand-name">Merrick Hale<br>Consulting Inc.</span>
</header>

<section class="business-card card--white">
  <div class="card-brand"><span class="brand-square"></span><span class="brand-name">Merrick Hale Consulting Inc.</span></div>
  <div class="card-divider"></div>
  <div class="card-holder">
    <p class="holder-name">XXXXXX J Hale, PMP</p>
    <p class="holder-title">Principle</p>
  </div>
  <ul class="contact-list">
    <li><svg><use href="#icon-phone"/></svg>(555) 013-2748</li>
    <li><svg><use href="#icon-mail"/></svg>merrick.hale@xxxxx.xxx</li>
    <li><svg><use href="#icon-web"/></svg>www.merrickhale.com</li>
  </ul>
  <div class="card-values">
    <p class="values-line">Honesty<span class="dot"></span>Integrity<span class="dot"></span>Respect</p>
    <p class="experience-line"><span class="accent">35+ years experience in</span> <span class="plain">Civil Infrastructure Construction</span> <span class="accent">&amp;</span> <span class="plain">Maintenance</span></p>
  </div>
</section>

<section class="business-card card--black">
  <div class="card-brand"><span class="brand-square"></span><span class="brand-name">Merrick Hale Consulting Inc.</span></div>
  <div class="card-divider"></div>
  <div class="card-holder">
    <p class="holder-name">XXXXXX J Hale, PMP</p>
    <p class="holder-title">Principle</p>
  </div>
  <ul class="contact-list">
    <li><svg><use href="#icon-phone"/></svg>(555) 013-2748</li>
    <li><svg><use href="#icon-mail"/></svg>merrick.hale@xxxxx.xxx</li>
    <li><svg><use href="#icon-web"/></svg>www.merrickhale.com</li>
  </ul>
  <div class="card-values">
    <p class="values-line">Honesty<span class="dot"></span>Integrity<span class="dot"></span>Respect</p>
    <p class="experience-line"><span class="accent">35+ years experience in</span> <span class="plain">Civil Infrastructure Construction</span> <span class="accent">&amp;</span> <span class="plain">Maintenance</span></p>
  </div>
</section>

<section class="business-card card--blue">
  <div class="card-brand"><span class="brand-square"></span><span class="brand-name">Merrick Hale Consulting Inc.</span></div>
  <div class="card-divider"></div>
  <div class="card-holder">
    <p class="holder-name">XXXXXX J Hale, PMP</p>
    <p class="holder-title">Principle</p>
  </div>
  <ul class="contact-list">
    <li><svg><use href="#icon-phone"/></svg>(555) 013-2748</li>
    <li><svg><use href="#icon-mail"/></svg>merrick.hale@xxxxx.xxx</li>
    <li><svg><use href="#icon-web"/></svg>www.merrickhale.com</li>
  </ul>
  <div class="card-values">
    <p class="values-line">Honesty<span class="dot"></span>Integrity<span class="dot"></span>Respect</p>
    <p class="experience-line"><span class="accent">35+ years experience in</span> <span class="plain">Civil Infrastructure Construction</span> <span class="accent">&amp;</span> <span class="plain">Maintenance</span></p>
  </div>
</section>

</body>
</html>
```